Lottery Website Design

Full website design, where you can take part on a lottery. Inkl Logo. The website is already developed: http://www.mondfeld-ziehung.de
I like the modern fullscreen design from
http://www.prairieraffle.com/en-us/home.html
but the field for using the lottery right away should be present as well an the first screen like here:
https://www.glueckstrommel.de/lotto/
Colour Scheme:
Red and Yellow?
Responsive design and coding (HTML & CSS).
The current website layout with bootstrap design ist http://www.mondfeld-ziehung.de - the logo may be similar to favicon
Feel free to ask! :)
As always I am looking forward for your great ideas!
Updates

```html
<!DOCTYPE html>
<html lang="de">
<head>
<meta charset="utf-8">
<title>Mondfeld – Lotto online</title>
<link rel="stylesheet" href="https://fonts.googleapis.com/css2?family=Lilita+One&family=Source+Sans+3:wght@400;600;700&display=swap">
<style>
:root{
  --sky:#82cdf0;
  --sky-light:#b4e2f7;
  --nav:#19a5de;
  --nav-dark:#0d86bd;
  --teal:#52ada4;
  --sand:#f8f1a8;
  --red:#d7222e;
  --wine:#8c1020;
  --orange:#f7931e;
  --orange-dark:#e2720c;
  --price:#1d7f7c;
  --ink:#3a3a3a;
  --night:#2d2d2d;
  --footer:#3e3e3e;
  --base:#1b1b1b;
  --muted:#b9b9b9;
  --white:#ffffff;
}
*{box-sizing:border-box;margin:0;padding:0}
html,body{width:690px;height:1200px;overflow:hidden}
body{font-family:"Source Sans 3",Arial,sans-serif;color:var(--ink);position:relative;background:var(--footer)}
.abs{position:absolute}
.display{font-family:"Lilita One",Impact,sans-serif;font-weight:400}

/* hero */
.hero{left:0;top:0;width:690px;height:286px;background:radial-gradient(circle at 345px 60px,var(--sky-light),var(--sky) 70%)}
.hero-scenery{left:0;top:232px;width:690px;height:54px;background:linear-gradient(180deg,rgba(82,173,164,0) 0%,rgba(82,173,164,.55) 100%)}
.tree{left:12px;top:168px;width:78px;height:118px;border-radius:40px 40px 6px 6px;background:linear-gradient(180deg,#8bc34a,#6aa13a)}
.brand{left:313px;top:28px;width:64px;height:64px;border-radius:50%;background:var(--white);display:flex;align-items:center;justify-content:center;font-family:"Lilita One",Impact,sans-serif;font-size:13px;color:var(--nav)}
.social-top{left:514px;top:70px;display:flex;gap:4px}
.social-top span{width:16px;height:16px;border-radius:50%;background:var(--white)}
.nav{left:108px;top:114px;width:474px;height:36px;background:var(--nav);display:flex;justify-content:space-around;align-items:center;padding:0 6px;z-index:2}
.nav a{color:var(--white);font-weight:700;font-size:8px;text-decoration:none;letter-spacing:.2px}
.ribbon{top:128px;width:30px;height:38px;background:var(--nav-dark)}
.ribbon.left{left:88px;clip-path:polygon(0 0,100% 0,100% 100%,0 100%,25% 50%)}
.ribbon.right{left:572px;clip-path:polygon(0 0,100% 0,75% 50%,100% 100%,0 100%)}
.jackpot{left:0;top:170px;width:690px;text-align:center;font-size:43px;line-height:1.1;color:var(--red);letter-spacing:1px}
.next-draw{left:0;top:225px;width:690px;text-align:center;color:var(--white);font-weight:700;font-size:8px}
.arrow{top:200px}
.btn{background:var(--orange);color:var(--white);font-weight:700;font-size:7px;border-radius:2px;border-bottom:2px solid var(--orange-dark);display:flex;align-items:center;justify-content:center}
.hero-buy{left:318px;top:248px;width:42px;height:19px}

/* games */
.games{left:0;top:286px;width:690px;height:200px;background:var(--teal)}
.card{top:314px;width:112px;height:160px;background:var(--white);border:2px solid #7fd0d4;z-index:3;overflow:hidden}
.card-photo{width:100%;height:82px}
.card-price{margin:9px 0 0 7px;font-weight:700;font-size:13px;line-height:16px;color:var(--price)}
.card-info{margin:5px 0 0 7px;font-size:6.5px;font-weight:600;line-height:9px;color:#222}
.card .btn{margin:6px 0 0 6px;width:42px;height:18px}
.ridge{left:0;top:476px;width:690px;height:70px;background:linear-gradient(180deg,var(--teal),var(--sand))}

/* play section */
.play{left:0;top:546px;width:690px;height:290px;background:var(--sand)}
.section-title{left:104px;top:568px;font-size:14px;color:var(--ink)}
.ticket{left:104px;top:602px;width:370px;height:124px;background:#fbf7d9;padding:3px;display:grid;grid-template-columns:repeat(6,1fr);gap:3px}
.ticket span{background:repeating-linear-gradient(0deg,#e8e8e8 0 1px,transparent 1px 6px),repeating-linear-gradient(90deg,#e8e8e8 0 1px,#f7f7f7 1px 6px);display:flex;align-items:center;justify-content:center;font-size:36px;color:#d6d6d6;font-weight:400}
.promo-title{left:489px;top:604px;font-size:15px;color:var(--wine);line-height:1.45}
.promo-text{left:489px;top:650px;width:105px;font-size:8.5px;line-height:1.3;color:#555}
.promo-buy{left:486px;top:717px;width:43px;height:19px}
.control-label{top:750px;font-size:11.5px;font-weight:600;color:var(--ink)}
.chips{top:780px;display:flex;gap:3px;align-items:center}
.chips span{height:22px;min-width:27px;padding:0 5px;background:#fbf8dc;font-size:11px;display:flex;align-items:center;justify-content:center;color:#333}
.chips span.on{background:var(--wine);color:var(--white)}

/* skyline */
.skyline{left:0;top:832px;width:690px;height:112px;background:linear-gradient(180deg,var(--sand) 0%,var(--night) 45%,var(--night) 100%)}

/* footer */
.form-title{left:104px;top:950px;font-size:14px;color:var(--white)}
.field{left:104px;width:126px;background:var(--white);border-radius:14px;font-size:8px;color:#777;padding:8px 14px}
.submit{left:241px;top:1090px;width:63px;height:25px;border-radius:13px;background:var(--orange);border-bottom:2px solid var(--orange-dark);color:var(--white);font-family:"Lilita One",Impact,sans-serif;font-size:10px;display:flex;align-items:center;justify-content:center}
.contact{left:380px;display:flex;gap:9px;align-items:flex-start;color:var(--muted);font-size:7.5px;line-height:1.5}
.contact strong{font-weight:600;font-size:8px}
.contact svg{flex:none}
.social-foot{left:377px;top:1079px;display:flex;gap:10px}
.social-foot span{width:20px;height:20px;border-radius:50%;border:1px solid #666}
.base{left:0;top:1144px;width:690px;height:56px;background:var(--base)}
.base-links{left:104px;top:1159px;display:flex;font-size:6.5px;color:#aaa}
.base-links a{color:#aaa;text-decoration:none;margin-right:18px}
.copyright{left:104px;top:1174px;font-size:6.5px;color:#888}
</style>
</head>
<body>

<section class="abs hero"></section>
<div class="abs hero-scenery" role="img" aria-label="Hügelkette im Hintergrund"></div>
<div class="abs tree" role="img" aria-label="Illustrierter Baum mit Büschen"></div>
<div class="abs brand">Mondfeld</div>
<div class="abs social-top"><span></span><span></span><span></span></div>

<div class="abs ribbon left"></div>
<div class="abs ribbon right"></div>
<nav class="abs nav">
  <a href="#">GAMES</a><a href="#">WINNING</a><a href="#">PROMOTIONS</a><a href="#">GIVING BACK</a><a href="#">PLAY NOW</a><a href="#">MY ACCOUNT</a><a href="#">REGISTER</a>
</nav>

<svg class="abs arrow" style="left:132px" width="10" height="16" viewBox="0 0 10 16"><path d="M8 1 2 8l6 7" fill="none" stroke="#fff" stroke-width="1.5"/></svg>
<svg class="abs arrow" style="left:546px" width="10" height="16" viewBox="0 0 10 16"><path d="M2 1l6 7-6 7" fill="none" stroke="#fff" stroke-width="1.5"/></svg>
<div class="abs jackpot display">$60,000,000</div>
<div class="abs next-draw">Next Draw: Sat, Jul 19</div>
<div class="abs btn hero-buy">Buy Now</div>

<section class="abs games"></section>
<div class="abs ridge" role="img" aria-label="Bergkette als Übergang"></div>
<article class="abs card" style="left:104px">
  <div class="card-photo" role="img" aria-label="Foto eines Roulettekessels" style="background:linear-gradient(135deg,#5b3a2a,#b9c4cf)"></div>
  <p class="card-price">$ 50,000,000</p>
  <p class="card-info">Next Draw: Fri, Jul 18<br>10:00 PM CST</p>
  <div class="btn">Buy Now</div>
</article>
<article class="abs card" style="left:228px">
  <div class="card-photo" role="img" aria-label="Foto eines Spielautomaten mit Kartenbildschirm" style="background:linear-gradient(135deg,#1d2b5a,#3e7fc4)"></div>
  <p class="card-price">$ 3,750,000</p>
  <p class="card-info">Next Draw: Fri, Jul 18<br>10:00 PM CST</p>
  <div class="btn">Buy Now</div>
</article>
<article class="abs card" style="left:350px">
  <div class="card-photo" role="img" aria-label="Foto eines roten Roulettetisches" style="background:linear-gradient(135deg,#7a1a12,#c4582e)"></div>
  <p class="card-price">$ 500,000</p>
  <p class="card-info">Next Draw: Fri, Jul 18<br>10:00 PM CST</p>
  <div class="btn">Buy Now</div>
</article>
<article class="abs card" style="left:473px">
  <div class="card-photo" role="img" aria-label="Foto eines Spieltisches mit Karten und Chips" style="background:linear-gradient(135deg,#1f7a3a,#3aa05a)"></div>
  <p class="card-price">$ 50,000</p>
  <p class="card-info">Next Draw: Fri, Jul 18<br>10:00 PM CST</p>
  <div class="btn">Buy Now</div>
</article>

<section class="abs play"></section>
<h2 class="abs section-title display">WIR SIND AUF SENDUNG!</h2>
<div class="abs ticket">
  <span>1</span><span>2</span><span>3</span><span>4</span><span>5</span><span>6</span>
  <span>7</span><span>8</span><span>9</span><span>10</span><span>11</span><span>12</span>
</div>
<h3 class="abs promo-title display">Wir sind auf<br>Sendung!</h3>
<p class="abs promo-text">Schau. Schau. Wir kennen uns aus dem TV. Online tippen. Günstiger als am Kiosk. Jetzt 6 Kreuze gratis für Neukunden.</p>
<div class="abs btn promo-buy">Buy Now</div>

<p class="abs control-label" style="left:104px">Quicktipps (Zufallszahlen)</p>
<p class="abs control-label" style="left:261px">Ziehung</p>
<p class="abs control-label" style="left:370px">Wochenlaufzeit</p>
<div class="abs chips" style="left:104px">
  <span>+1</span><span>+2</span><span>+4</span><span>+12</span>
  <svg width="14" height="16" viewBox="0 0 14 16"><path d="M2 4h10M5 4V2h4v2M3 4l1 11h6l1-11" fill="none" stroke="#444" stroke-width="1.6"/></svg>
</div>
<div class="abs chips" style="left:261px"><span>MI</span><span class="on">SA</span><span>MI / SA</span></div>
<div class="abs chips" style="left:373px;gap:6px"><span class="on">1</span><span>2</span><span>3</span></div>

<div class="abs skyline" role="img" aria-label="Silhouette einer Stadt vor der Sonne"></div>

<h2 class="abs form-title display">Enquiry Form</h2>
<div class="abs field" style="top:978px;height:26px">Name</div>
<div class="abs field" style="top:1012px;height:26px">Email</div>
<div class="abs field" style="top:1047px;height:73px;border-radius:18px">Message</div>
<div class="abs submit">Submit</div>

<div class="abs contact" style="top:974px">
  <svg width="9" height="12" viewBox="0 0 9 12"><path d="M4.5 0A4.5 4.5 0 0 0 0 4.5C0 8 4.5 12 4.5 12S9 8 9 4.5A4.5 4.5 0 0 0 4.5 0zm0 6.3a1.8 1.8 0 1 1 0-3.6 1.8 1.8 0 0 1 0 3.6z" fill="#fff"/></svg>
  <p>Harlow Civic Hall<br>240 W. Larkspur Ave, 5th Floor, Brookvale, IL 60999<br>8:30 AM–4:30 PM</p>
</div>
<div class="abs contact" style="top:1019px">
  <svg width="11" height="11" viewBox="0 0 11 11"><path d="M2.2 0 4 2.6 2.8 3.8a7 7 0 0 0 4.4 4.4L8.4 7 11 8.8 9.8 11C4.4 11 0 6.6 0 1.2z" fill="#fff"/></svg>
  <strong>Player Hotline: 1-800-555-0142</strong>
</div>
<div class="abs contact" style="top:1050px">
  <svg width="12" height="9" viewBox="0 0 12 9"><rect x=".5" y=".5" width="11" height="8" fill="none" stroke="#fff"/><path d="M.5.5 6 5l5.5-4.5" fill="none" stroke="#fff"/></svg>
  <strong>Email: Info@PrairieRaffle.com</strong>
</div>
<div class="abs social-foot"><span></span><span></span><span></span><span></span><span></span></div>

<footer class="abs base"></footer>
<nav class="abs base-links">
  <a href="#">Help</a><a href="#">Contact Us</a><a href="#">Be Scam Smart</a><a href="#">Lottery Sitemap</a><a href="#">Privacy Information</a><a href="#">Web Accessibility</a><a href="#">Responsible Gaming</a>
</nav>
<p class="abs copyright">© 2014 mondfeld-ziehung.de. All rights reserved.</p>

</body>
</html>
```